依頼詳細
http://mirokan.jp/
こちらのコーポレーションサイトのデザイン追加と修正をお願いいたします。

①トップで使用している街並みの写真(東京の写真)を
東京以外の街並みでかっこいい雰囲気の写真に差し替えをお願いいたします。
青っぽい感じが希望ですが、雰囲気に合わせて今の色から変更していただいてOKです。
テキストの字体も雰囲気に合わせて変更していただいて大丈夫です。

②サイト内にある下記の項目をポップアップで表示させるようにしたいと思っており、その際に表示される各項目のデザイン作成をお願いいたします。
各項目ともテキストはそのままで、参考サイトのトップのように写真の上に文字があって、各事業の文字を大きく、説明は小さく入れてください。
写真・フィルターは①の雰囲気に合うようお任せいたします。
フィルターはあってもなくてもいいです。

・不動産仲介事業
・リフォームリノベーション事業
・注文住宅事業
・不動産コンサルティング

③右上に表示されている項目(Home・Service・Company・Contact)に
Greetingsを追加して下さい。
※代表挨拶の意味で追加したいのですが
ほかに良い表記がありましたらそちらでお願いいたします。

④conpanyの上に
③で追加したGreetingsの項目を追加してください。
※テキストはあとから入れたいので、文字のボリューム感がわかるように
テストのテキストを入れていただけると助かります。

⑤Companyの横に添付写真を入れられたらお願いいたします。
※こちらの写真は後ほど添付いたします。

参考サイト
https://palvestaworks.com/

何か説明など足りない点がございましたら
お手数ですが直接ご質問をお願いいたします。

よろしくお願いいたします。
サイトURL
http://mirokan.jp/
ページ数
1ページ
希望イメージ
シンプル 複雑
単色 カラフル
暗い 明るい
日常 高級
遊び心 厳粛
未来的 伝統的
女性的 男性的
希望する色
青系、水色系、無彩色系
納品ファイル
• イラストレーター形式 (.ai)
• フォトショップ形式 (.psd)
補足説明
company部分の写真の追加となります。
3枚添付していますので良さそうな写真でお願い致します。
※消毒のボトルなど、見栄え悪そうなものは加工していただいて構いません。

よろしくお願い致します。
申し訳ございません。
下記の項目の点を修正お願いいたします。

【修正前】
①トップで使用している街並みの写真(東京の写真)を

【修正後】
空、オフィス系や建築会社系、機械的デザイン等
いろんなパターンで見てみたいので
街並みと人間が入っていないものでお願いいたします。

よろしくお願いいたします。
■ 選んだ理由

弊社サイトに一番合っていたので当選とさせていただきました。

■ 提案者全員のお礼・コメント

ご参加ありがとうございました。

```html
<!DOCTYPE html>
<html lang="ja">
<head>
<meta charset="utf-8">
<title>株式会社 Mirokan</title>
<link rel="stylesheet" href="https://fonts.googleapis.com/css2?family=Noto+Serif+JP:wght@400;500;700&family=Libre+Baskerville&display=swap">
<style>
  :root {
    --blue: #3f86d6;
    --blue-deep: #2f6fb8;
    --blue-soft: #a9d6ea;
    --ink: #333;
    --grey: #666;
    --grey-tab: #5c5c5c;
    --dark-btn: #4a3f3a;
    --white: #fff;
    --panel: rgba(52, 62, 72, .62);
  }
  * { margin: 0; padding: 0; box-sizing: border-box; }
  html, body { width: 1200px; height: 3828px; overflow: hidden; }
  body { position: relative; background: var(--white); color: var(--ink); font-family: "Noto Serif JP", serif; }
  .abs { position: absolute; }

  /* header */
  .site-header { left: 0; top: 0; width: 1200px; height: 140px; }
  .brand { left: 120px; top: 48px; font-size: 30px; font-weight: 700; letter-spacing: 2px; color: var(--ink); }
  .brand small { font-size: 20px; margin-right: 10px; }
  .header-tel { left: 745px; top: 44px; font-size: 38px; letter-spacing: 4px; color: #777; font-family: "Libre Baskerville", serif; }
  .global-nav { left: 0; top: 140px; width: 1200px; height: 56px; background: var(--blue); }
  .global-nav ul { position: absolute; left: 205px; top: 18px; list-style: none; display: flex; gap: 14px; color: var(--white); font-size: 15px; letter-spacing: 3px; font-family: "Libre Baskerville", serif; }
  .global-nav li + li::before { content: "•"; margin-right: 14px; }
  .nav-contact { left: 868px; top: 150px; width: 172px; height: 36px; background: var(--dark-btn); color: var(--white); font-size: 14px; letter-spacing: 2px; text-align: center; line-height: 36px; }

  /* hero */
  .hero { left: 0; top: 196px; width: 1200px; height: 604px; background: linear-gradient(180deg, #cfe6f5 0%, #8ebfe3 35%, #4f85b5 65%, #34597f 100%); }
  .hero-copy { right: 30px; top: 40px; display: flex; flex-direction: row-reverse; gap: 22px; }
  .hero-copy p { writing-mode: vertical-rl; color: var(--white); font-size: 26px; letter-spacing: 8px; font-weight: 500; text-shadow: 0 1px 4px rgba(0,0,0,.25); }

  /* section titles */
  .section-title { left: 0; width: 1200px; text-align: center; }
  .section-title h2 { font-family: "Libre Baskerville", serif; font-weight: 400; font-size: 42px; letter-spacing: 10px; color: #555; }
  .section-title span { display: block; margin-top: 6px; font-size: 12px; letter-spacing: 3px; color: #888; }
  .section-title span::before, .section-title span::after { content: ""; display: inline-block; width: 40px; height: 1px; background: #aaa; vertical-align: middle; margin: 0 10px; }

  /* service */
  .service { left: 0; top: 960px; width: 1200px; height: 580px; background: var(--blue-soft); }
  .service-photo { left: 80px; top: 970px; width: 1040px; height: 230px; background: linear-gradient(120deg, #2e2f33 0%, #55585e 50%, #3a3b3f 100%); }
  .service-label { left: 410px; top: 1040px; width: 380px; height: 46px; border-radius: 23px; background: var(--blue); color: var(--white); font-size: 22px; letter-spacing: 4px; text-align: center; line-height: 46px; }
  .service-text { left: 80px; top: 1200px; width: 1040px; height: 180px; background: var(--white); padding: 28px 110px; font-size: 15px; line-height: 2; color: var(--ink); }
  .service-tabs { left: 80px; top: 1390px; width: 1040px; height: 140px; display: flex; gap: 4px; }
  .tab { flex: 1; background: var(--grey-tab); color: var(--white); display: flex; align-items: center; justify-content: center; gap: 16px; font-size: 17px; line-height: 1.5; }
  .tab.is-active { background: #5b86c5; }
  .tab svg { width: 44px; height: 44px; }

  /* greetings */
  .greetings { left: 0; top: 1670px; width: 1200px; height: 480px; background: linear-gradient(135deg, #2b211b 0%, #5b4332 40%, #3d2d22 75%, #1f1712 100%); }
  .greetings-body { left: 210px; top: 1700px; width: 780px; color: #f2ece6; }
  .greetings-body h3 { text-align: center; font-size: 22px; letter-spacing: 8px; font-weight: 500; margin-bottom: 22px; }
  .greetings-body p { font-size: 14px; line-height: 2.05; letter-spacing: 1px; margin-bottom: 14px; }

  /* company */
  .company-lead { left: 0; top: 2210px; width: 1200px; text-align: center; color: var(--blue-deep); font-size: 26px; letter-spacing: 4px; line-height: 1.6; }
  .company-photo-left { left: 80px; top: 2320px; width: 560px; height: 490px; background: linear-gradient(180deg, #a8b3bd 0%, #7c858c 50%, #c9c6bf 100%); }
  .company-photo-right { left: 640px; top: 2320px; width: 480px; height: 350px; background: linear-gradient(160deg, #7f9a6a 0%, #4d6a3f 45%, #9fa8a6 100%); }
  .company-panel { left: 340px; top: 2330px; width: 480px; height: 330px; background: var(--panel); padding: 18px 30px; color: var(--white); }
  .company-panel h3 { font-family: "Libre Baskerville", serif; font-weight: 400; font-size: 32px; letter-spacing: 8px; color: var(--white); margin-bottom: 8px; }
  .company-table { width: 100%; border-collapse: collapse; font-size: 13px; color: var(--white); }
  .company-table th, .company-table td { border-bottom: 1px solid rgba(255,255,255,.45); padding: 5px 6px; text-align: left; font-weight: 400; }
  .company-table th { width: 96px; letter-spacing: 2px; }
  .company-card { left: 600px; top: 2670px; width: 520px; height: 140px; background: var(--blue); color: var(--white); padding: 18px 30px; }
  .company-card .name { font-size: 26px; font-weight: 700; letter-spacing: 2px; }
  .company-card .name small { font-size: 18px; margin-right: 8px; }
  .company-card .tel { font-family: "Libre Baskerville", serif; font-size: 34px; letter-spacing: 3px; display: flex; align-items: center; gap: 10px; margin-top: 4px; }
  .company-card .addr { position: absolute; right: 24px; top: 30px; font-size: 12px; line-height: 1.6; text-align: right; }

  /* contact */
  .contact { left: 0; top: 3040px; width: 1200px; height: 520px; background: linear-gradient(120deg, #c9a98a 0%, #efe6dc 35%, #f4efe9 60%, #6a5a50 100%); }
  .contact-form { left: 300px; top: 3070px; width: 600px; }
  .field { display: flex; height: 44px; margin-bottom: 12px; }
  .field label { width: 130px; background: rgba(255,255,255,.55); font-size: 13px; line-height: 44px; padding-left: 16px; color: var(--ink); }
  .field .input { flex: 1; background: var(--white); font-size: 12px; color: #aaa; line-height: 44px; padding-left: 14px; }
  .field.is-tall { height: 170px; }
  .submit { left: 540px; top: 3440px; width: 120px; height: 42px; border-radius: 21px; background: var(--blue); color: var(--white); text-align: center; line-height: 42px; font-size: 15px; letter-spacing: 6px; }

  .site-footer { left: 0; top: 3690px; width: 1200px; text-align: center; font-size: 12px; letter-spacing: 2px; color: #888; font-family: "Libre Baskerville", serif; }
</style>
</head>
<body>

<header class="abs site-header">
  <div class="abs brand"><small>株式会社</small>Mirokan</div>
  <div class="abs header-tel">03-4821-6037</div>
</header>
<nav class="abs global-nav">
  <ul><li>Home</li><li>Service</li><li>Greetings</li><li>Company</li><li>Contact</li></ul>
</nav>
<div class="abs nav-contact">お問い合わせ</div>

<section class="abs hero" role="img" aria-label="青空の下に立ち並ぶ高層ビル群の写真">
  <div class="abs hero-copy">
    <p>ひとりひとりの</p>
    <p>マイホームの夢を</p>
    <p>叶えるために</p>
    <p>お客さまの声を</p>
    <p>大切にして</p>
    <p>最適なプランを</p>
    <p>ご提案いたします</p>
  </div>
</section>

<div class="abs section-title" style="top:860px"><h2>Service</h2><span>サービス</span></div>
<section class="abs service"></section>
<div class="abs service-photo" role="img" aria-label="タブレットを操作しながら打ち合わせをする手元の写真"></div>
<div class="abs service-label">不動産仲介事業</div>
<div class="abs service-text">
  <p>Mirokanでは「新築一戸建」「中古マンション」「中古戸建」「土地」の仲介だけでなく、購入から売却まで住まいのご相談、住宅ローンや保険、税金関係についてもしっかりとサポートさせていただきます。お客様の大切な不動産取引を安心してお任せいただけるよう、誠実に対応いたします。</p>
</div>
<div class="abs service-tabs">
  <div class="tab is-active">
    <svg viewBox="0 0 44 44" fill="none" stroke="#fff" stroke-width="2"><path d="M6 22 22 8l16 14"/><path d="M11 19v17h22V19"/><rect x="18" y="26" width="8" height="10"/></svg>
    <span>不動産<br>仲介事業</span>
  </div>
  <div class="tab">
    <svg viewBox="0 0 44 44" fill="none" stroke="#fff" stroke-width="2"><path d="M6 22 22 8l16 14"/><path d="M11 19v17h22V19"/><path d="m17 30 10-10 3 3-10 10h-3z"/></svg>
    <span>リフォーム<br>リノベーション事業</span>
  </div>
  <div class="tab">
    <svg viewBox="0 0 44 44" fill="none" stroke="#fff" stroke-width="2"><path d="M6 22 22 8l16 14"/><path d="M11 19v17h22V19"/><rect x="17" y="23" width="10" height="8"/></svg>
    <span>注文住宅<br>事業</span>
  </div>
  <div class="tab">
    <svg viewBox="0 0 44 44" fill="none" stroke="#fff" stroke-width="2"><path d="M6 22 22 8l16 14"/><path d="M11 19v17h22V19"/><circle cx="22" cy="27" r="4"/></svg>
    <span>不動産<br>コンサルティング</span>
  </div>
</div>

<div class="abs section-title" style="top:1560px"><h2>Greetings</h2><span>ごあいさつ</span></div>
<section class="abs greetings" role="img" aria-label="木目のデスクに置かれたノートとペンの写真"></section>
<div class="abs greetings-body">
  <h3>ご挨拶</h3>
  <p>日頃より格別のご愛顧を賜り、誠にありがとうございます。私たちは地域に根ざした不動産会社として、お客様一人ひとりの暮らしに寄り添い、住まい探しから売却、リフォームまで幅広くお手伝いしてまいりました。これからも信頼される会社であり続けるよう努めてまいります。</p>
  <p>住まいは人生の大切な基盤です。だからこそ、私たちはお客様のお話にしっかりと耳を傾け、最適なご提案をすることを何より大切にしています。小さな疑問やご不安にも丁寧にお答えし、納得していただけるまで誠実にサポートいたします。</p>
  <p>今後とも社員一同、より良いサービスの提供に全力で取り組んでまいります。変わらぬご支援を賜りますよう、心よりお願い申し上げます。</p>
</div>

<div class="abs company-lead">不動産のことなら、<br>どうぞお気軽にご相談下さい。</div>
<div class="abs company-photo-left" role="img" aria-label="オフィス入口と室内の写真"></div>
<div class="abs company-photo-right" role="img" aria-label="街路樹のある通りに面した社屋の写真"></div>
<div class="abs company-panel">
  <h3>Company</h3>
  <table class="company-table">
    <tr><th>会社名</th><td>株式会社Mirokan</td></tr>
    <tr><th>所在地</th><td>東京都練馬区桜台2-8-14</td></tr>
    <tr><th>電話番号</th><td>03-4821-6037</td></tr>
    <tr><th>設立</th><td>2015年4月</td></tr>
    <tr><th>代表者</th><td>代表取締役 山田 太郎</td></tr>
    <tr><th>資本金</th><td>1,000万円</td></tr>
    <tr><th>事業内容</th><td>不動産仲介・リフォーム・注文住宅</td></tr>
    <tr><th>免許番号</th><td>東京都知事(2)第00000号</td></tr>
  </table>
</div>
<div class="abs company-card">
  <div class="name"><small>株式会社</small>Mirokan</div>
  <div class="tel">
    <svg width="30" height="30" viewBox="0 0 30 30" fill="none" stroke="#fff" stroke-width="2"><circle cx="15" cy="15" r="13"/><path d="M10 9c0 7 4 11 11 11l1-3-3-2-2 2c-2-1-3-2-4-4l2-2-2-3z" fill="#fff" stroke="none"/></svg>
    03-4821-6037
  </div>
  <div class="addr">東京都練馬区桜台2-8-14<br>10:00-19:00 水曜定休</div>
</div>

<div class="abs section-title" style="top:2900px"><h2>Contact</h2><span>コンタクト</span></div>
<section class="abs contact" role="img" aria-label="書類を前に相談する打ち合わせ風景の写真"></section>
<form class="abs contact-form">
  <div class="field"><label>お名前</label><div class="input">例）山田 太郎</div></div>
  <div class="field"><label>E-Mail</label><div class="input">info@mirokan.jp</div></div>
  <div class="field"><label>件名</label><div class="input">件名を入力してください</div></div>
  <div class="field is-tall"><label>お問い合わせ内容</label><div class="input">お問い合わせ内容をご記入ください</div></div>
</form>
<div class="abs submit">送信</div>

<footer class="abs site-footer">Copyright © 株式会社Mirokan. All Rights Reserved.</footer>

</body>
</html>
```